Zentrova - Creative Automation

We are a software house for Audio Visual Systems integration/automation and home automation. we develop innovative software to automate a variety of devices mainly related to audio visuals and we design touch panel user interfaces to control these systems.

We would like to see designs that stick to our colours and theme, which you can find on our webpage www.zentrova.com.au

The final design should communicate touch panels, innovation, software and automation.

Industry/Entity Type

Software

Requirements
Must have
• The business card must show the following information:
Name example : Derek Malloway
Qualification example: B Eng ICT(CompSys) Dip EngPrac
Title example : Control Systems Programmer
Mobile Phone, Company phone, Email address ,Company website

```html
<!DOCTYPE html>
<html lang="en">
<head>
<meta charset="utf-8">
<title>Zentrova - Creative Automation business card</title>
<link href="https://fonts.googleapis.com/css2?family=Didact+Gothic&family=Nunito:wght@700;800&display=swap" rel="stylesheet">
<style>
  :root {
    --brand-blue: #1a73c9;
    --brand-blue-deep: #0f5fb4;
    --brand-blue-light: #2a8ee0;
    --brand-green: #2e9e4f;
    --ink-grey: #555a60;
    --ink-soft: #7a7f85;
    --card-white: #ffffff;
    --backdrop: #e9ecef;
  }
  * { margin: 0; padding: 0; box-sizing: border-box; }
  html, body { width: 1200px; height: 675px; overflow: hidden; }
  body {
    background: var(--backdrop);
    font-family: "Didact Gothic", "Century Gothic", sans-serif;
    position: relative;
  }
  .card {
    position: absolute;
    top: 195px;
    width: 500px;
    height: 286px;
    border-radius: 2px;
    box-shadow: 0 6px 18px rgba(0,0,0,0.15);
    overflow: hidden;
  }
  .card--front { left: 70px; background: var(--card-white); }
  .card--back {
    left: 630px;
    background: radial-gradient(ellipse at 45% 60%, var(--brand-blue-light), var(--brand-blue-deep) 80%);
  }

  .wordmark { position: absolute; display: flex; align-items: center; gap: 12px; }
  .wordmark__square { width: 44px; height: 44px; border-radius: 6px; }
  .wordmark__name {
    font-family: "Nunito", "Century Gothic", sans-serif;
    font-weight: 800;
    font-size: 40px;
    line-height: 1;
    letter-spacing: -0.5px;
  }
  .wordmark__tagline {
    font-family: "Nunito", "Century Gothic", sans-serif;
    font-weight: 700;
    font-size: 8px;
    text-align: right;
    margin-top: 1px;
  }
  .card--front .wordmark { left: 34px; top: 52px; }
  .card--front .wordmark__square { background: var(--brand-blue); }
  .card--front .wordmark__name { color: var(--brand-green); }
  .card--front .wordmark__tagline { color: var(--brand-blue); }

  .card--back .wordmark { left: 50%; top: 50%; transform: translate(-50%, -50%); }
  .card--back .wordmark__square { background: var(--card-white); }
  .card--back .wordmark__name, .card--back .wordmark__tagline { color: var(--card-white); }

  .person { position: absolute; left: 120px; top: 126px; line-height: 1.25; }
  .person__name {
    font-family: "Nunito", "Century Gothic", sans-serif;
    font-weight: 800;
    font-size: 19px;
    color: var(--brand-blue);
  }
  .person__qualification { font-size: 11px; color: var(--ink-soft); }
  .person__title { font-size: 15px; color: var(--ink-grey); }

  .address { position: absolute; left: 140px; top: 200px; font-size: 14px; color: var(--ink-grey); line-height: 1.2; }
  .website {
    font-family: "Nunito", "Century Gothic", sans-serif;
    font-weight: 800;
    font-size: 14px;
    color: var(--brand-green);
  }

  .contacts { position: absolute; left: 300px; top: 78px; list-style: none; font-size: 13px; color: var(--ink-grey); line-height: 1.35; }
  .contacts li { display: flex; align-items: center; gap: 7px; }
  .contacts svg { width: 11px; height: 11px; fill: var(--brand-green); flex: none; }

  .card--back .website {
    position: absolute;
    right: 30px;
    top: 30px;
    color: var(--card-white);
    font-size: 12px;
  }
</style>
</head>
<body>
  <section class="card card--front" aria-label="Business card front">
    <div class="wordmark">
      <span class="wordmark__square"></span>
      <div>
        <div class="wordmark__name">zentrova</div>
        <div class="wordmark__tagline">Creative Automation</div>
      </div>
    </div>

    <div class="person">
      <div class="person__name">Derek Malloway</div>
      <div class="person__qualification">B Eng ICT (CompSys) Dip EngPrac</div>
      <div class="person__title">Principal</div>
    </div>

    <div class="address">
      <div>418 Larkfield Avenue</div>
      <div>Brookvale, IL 60712</div>
      <div class="website">www.zentrova.com.au</div>
    </div>

    <ul class="contacts">
      <li>
        <svg viewBox="0 0 12 12" aria-hidden="true"><path d="M1 4c0-2 2-3 5-3s5 1 5 3v1H8V3.5H4V5H1z M2 6h8l1 5H1z"/></svg>
        555.204.7731
      </li>
      <li>
        <svg viewBox="0 0 12 12" aria-hidden="true"><rect x="3" y="1" width="6" height="3"/><rect x="1" y="5" width="10" height="4" rx="1"/><rect x="3" y="8" width="6" height="3"/></svg>
        555.318.6402
      </li>
      <li>
        <svg viewBox="0 0 12 12" aria-hidden="true"><path d="M1 3h10v6H1z M1 3l5 4 5-4" stroke="#fff" stroke-width="0.8"/></svg>
        derek@zentrova.com.au
      </li>
    </ul>
  </section>

  <section class="card card--back" aria-label="Business card back">
    <div class="website">www.zentrova.com.au</div>
    <div class="wordmark">
      <span class="wordmark__square"></span>
      <div>
        <div class="wordmark__name">zentrova</div>
        <div class="wordmark__tagline">Creative Automation</div>
      </div>
    </div>
  </section>
</body>
</html>
```